Orvex Panel Flyer

I need a flyer designed for our Orvex Panel software service. Basically most of the content that is on the website (orvexpanel.com.au) but I have uploaded a couple of source files as well. Please continue with this blue colour scheme

Target Market(s)

Business owners

Industry/Entity Type

Software

Font styles to use
Sans Serif

Colors
0456a4

Requirements
Must have
• Content from orvexpanel.com.au and similar theme

```html
<!DOCTYPE html>
<html lang="en">
<head>
<meta charset="utf-8">
<title>Orvex Panel Flyer</title>
<link rel="stylesheet" href="https://fonts.googleapis.com/css2?family=Montserrat:wght@400;500;600;700;800&family=Poppins:wght@700&display=swap">
<style>
:root{
  --brand:#0456a4;
  --brand-deep:#0a2f7a;
  --violet:#4b3fc9;
  --sky:#2f8fe8;
  --navy:#0b1a33;
  --ink:#26313f;
  --paper:#f4f4f2;
  --stage:#d9d9d9;
  --white:#ffffff;
}
*{margin:0;padding:0;box-sizing:border-box}
html,body{width:1200px;height:3789px;overflow:hidden;background:var(--stage)}
.flyer{position:absolute;left:40px;top:1102px;width:1120px;height:1584px;background:var(--paper);overflow:hidden;font-family:"Montserrat",sans-serif;box-shadow:0 10px 40px rgba(0,0,0,.18)}
.flyer-shapes{position:absolute;inset:0}
.brand-name{position:absolute;left:36px;top:110px;width:420px;font-family:"Poppins",sans-serif;font-weight:700;font-size:80px;line-height:.95;color:var(--brand)}
.brand-name .word{display:block}
.brand-mark{display:inline-block;width:28px;height:28px;background:var(--brand);border-radius:50%;margin-right:16px;vertical-align:middle;position:relative;top:-6px}
.intro{position:absolute;left:36px;top:315px;width:430px;font-size:17px;line-height:1.5;color:var(--ink)}
.intro p+p{margin-top:4px}
.headline{position:absolute;left:36px;top:650px;color:var(--ink);text-transform:uppercase;line-height:1}
.headline .lead{display:block;font-size:34px;font-weight:700}
.headline .big{display:block;font-size:60px;font-weight:800;margin-top:6px}
.tagline{position:absolute;left:36px;top:790px;width:460px;font-size:17px;line-height:1.4;color:var(--ink)}
.features{position:absolute;left:700px;top:890px;width:390px;list-style:none;color:var(--white)}
.feature{position:relative;height:150px;padding-left:10px}
.feature h3{font-size:17px;font-weight:700;letter-spacing:.5px;text-transform:uppercase;margin-bottom:6px}
.feature p{font-size:13.5px;line-height:1.45;opacity:.92}
.feature-icon{position:absolute;left:-100px;top:-8px;width:68px;height:76px}
.claim{position:absolute;left:36px;top:1290px;color:var(--white);text-transform:uppercase;line-height:1.08;font-size:40px}
.claim .light{font-weight:400;display:block}
.claim .bold{font-weight:700;display:block}
</style>
</head>
<body>
<article class="flyer">
  <svg class="flyer-shapes" width="1120" height="1584" viewBox="0 0 1120 1584">
    <defs>
      <linearGradient id="panelGrad" x1="0" y1="0" x2="1" y2="1">
        <stop offset="0" stop-color="#2f8fe8"/>
        <stop offset=".55" stop-color="#0456a4"/>
        <stop offset="1" stop-color="#4b3fc9"/>
      </linearGradient>
      <linearGradient id="photoGrad" x1="0" y1="0" x2="1" y2="1">
        <stop offset="0" stop-color="#5a4a8f"/>
        <stop offset=".5" stop-color="#3a4f9a"/>
        <stop offset="1" stop-color="#1d2f6a"/>
      </linearGradient>
      <linearGradient id="darkGrad" x1="0" y1="0" x2="0" y2="1">
        <stop offset="0" stop-color="#1b3158"/>
        <stop offset="1" stop-color="#0b1a33"/>
      </linearGradient>
      <linearGradient id="deviceGrad" x1="0" y1="0" x2="1" y2="1">
        <stop offset="0" stop-color="#e9ecf5"/>
        <stop offset=".6" stop-color="#c9cfe6"/>
        <stop offset="1" stop-color="#9aa3c8"/>
      </linearGradient>
    </defs>
    <rect class="dark-band" x="0" y="880" width="1120" height="704" fill="url(#darkGrad)"/>
    <g role="img" aria-label="Photo of hands typing on a laptop keyboard">
      <polygon points="620,0 1120,0 1120,560 640,620 500,300" fill="url(#photoGrad)"/>
    </g>
    <polygon class="accent-triangle" points="520,0 680,0 600,130" fill="#0a2f7a" opacity=".85"/>
    <polygon class="accent-triangle" points="600,540 740,600 620,680" fill="#0456a4"/>
    <polygon class="feature-panel" points="640,620 1120,560 1120,1584 660,1584 660,960 580,880" fill="url(#panelGrad)"/>
    <g role="img" aria-label="Laptop, tablet and phone showing sales report dashboards">
      <rect x="20" y="930" width="500" height="330" rx="14" fill="url(#deviceGrad)"/>
    </g>
  </svg>

  <div class="brand-name"><span class="word"><span class="brand-mark"></span>Orvex</span><span class="word">Panel</span></div>

  <div class="intro">
    <p>We specialise in providing reporting and staff performance management tools to the Veltra Licensed Store (VLS) channel.</p>
    <p>With our Orvex Panel service, our aim to help you boost performance in your teams and increase efficiency by providing comprehensive reporting and performance management tools that help you keep your finger on the pulse of your business.</p>
  </div>

  <h2 class="headline"><span class="lead">Know your</span><span class="big">Numbers.</span></h2>
  <p class="tagline">Simple and interactive reports that highlight the main opportunities in your sales team.</p>

  <ul class="features">
    <li class="feature">
      <svg class="feature-icon" viewBox="0 0 68 76"><polygon points="34,2 66,20 66,56 34,74 2,56 2,20" fill="none" stroke="#fff" stroke-width="3"/><path d="M22 50 L46 26 M36 26 H46 V36" fill="none" stroke="#fff" stroke-width="3"/></svg>
      <h3>Performance</h3>
      <p>Less time collecting data, more time coaching your team. Orvex Panel has been proven to drive positive focus out of a managers day.</p>
    </li>
    <li class="feature">
      <svg class="feature-icon" viewBox="0 0 68 76"><polygon points="34,2 66,20 66,56 34,74 2,56 2,20" fill="none" stroke="#fff" stroke-width="3"/><rect x="25" y="22" width="18" height="32" rx="3" fill="none" stroke="#fff" stroke-width="3"/></svg>
      <h3>Mobile Friendly</h3>
      <p>All our reports are fully optimised to be viewed on any platform including smartphones, tablets and PCs.</p>
    </li>
    <li class="feature">
      <svg class="feature-icon" viewBox="0 0 68 76"><polygon points="34,2 66,20 66,56 34,74 2,56 2,20" fill="none" stroke="#fff" stroke-width="3"/><circle cx="34" cy="38" r="13" fill="none" stroke="#fff" stroke-width="3"/><path d="M34 31 V38 L40 42" fill="none" stroke="#fff" stroke-width="3"/></svg>
      <h3>Responsive</h3>
      <p>We are always on top of the current priorities in the channel and respond quickly to give you the insights you need to be proactive.</p>
    </li>
    <li class="feature">
      <svg class="feature-icon" viewBox="0 0 68 76"><polygon points="34,2 66,20 66,56 34,74 2,56 2,20" fill="none" stroke="#fff" stroke-width="3"/><circle cx="28" cy="44" r="8" fill="none" stroke="#fff" stroke-width="3"/><circle cx="42" cy="30" r="6" fill="none" stroke="#fff" stroke-width="3"/></svg>
      <h3>Customisable</h3>
      <p>We offer a range of customised reporting solutions including traffic reporting, commission trackers, inventory management and just about anything else.</p>
    </li>
  </ul>

  <p class="claim">
    <span class="light">Customer</span>
    <span class="bold">Experience insights.</span>
    <span class="light">Custom</span>
    <span class="bold">Built solutions.</span>
  </p>
</article>
</body>
</html>
```